Dar Nakheel Business Card Design Project

-Project: Redesign Dar Nakheel Business Cards
-What we do: Dar Nakheel is the leading Arabic electronic content service provider. We are the industry’s only provider of full-text searchable electronic databases of peer-reviewed and copyright protected Arabic publications.Dar Nakheel combines publishing and library industry expertise with best-in-class
technology to enable academics, researchers and library users to efficiently discover and access thousands of electronic publications from the Arab world’s leading publishers and research institutes.
-Our Products: eBooks,eJournals, eReports & eDissertations.
-Website: www.darnakheel-demo.com
Updates

Hi Designers,

Good job so far, but we would like to see few more options with a twist on a more visual direction.
In particular, we would like to see represented the technology which refers to our industry; we want to show that our company is an hi-tech pioneer in the publishing industry.

Hi-tech, elegance and electronic publishing industry in one concept.

If you need, you can have a glance of our eContent Online Platform  at http://portal.quillstack-demo.com/lib/darnakheel/home.action
where eBooks, eJournals, Academic eDissertations and eReports (all in arabic language) are available for demo purposes.

So far we represented our self through the visual concept of electronic bookshelves on which all our content types are displayed. You could start from there if you wish.

Thank you and wish you a creative work!
 

Reason: Because of Christmas & New Year's Vacation. Our Office will be off. Thanks,

We need a new business cards designs as follows:

-Business Card Design: White, simple and clean ... something similar to Pebble Co. corporate identity. 

-Color: only use White, Blue and Grey. 
BLUE:

R: 108 G:204 B: 242

Grey:

R: 148 G: 149 B: 153

-Key words describing our identity: professional, technology, transparent and advancement. 

If you have any questions or comments please email me rkhatib@darnakheel-demo.com

Target Market(s)

Dar Nakheel target are divided into two: 1) Publishers 2) Universities, Libraries and Research Centers World Wide

Industry/Entity Type

Electronic

Requirements
Must have
• Dar Nakheel Logo
Dar Nakheel Colors
Dar Nakheel Font: Tahoma
Dar Nakheel Business Cards text details (as design attached)
The Business card must be bilingual
Make sure the design will be a good starting point to be re-used on other material type.
Design of BC must be double face.
Nice to have
• Some brands names that we like:
http://marlowgrange-demo.com/
http://shelf.ravencourt-demo.com/

```html
<!DOCTYPE html>
<html lang="en">
<head>
<meta charset="utf-8">
<title>Dar Nakheel – Business Card</title>
<link rel="stylesheet" href="https://fonts.googleapis.com/css2?family=Noto+Sans:wght@400;700&family=Noto+Sans+Arabic:wght@400;500&display=swap">
<style>
  :root {
    --brand-blue: #6cccf2;
    --brand-grey: #949599;
    --ink: #000000;
    --paper: #ffffff;
    --band: #eef7fc;
  }
  html, body {
    margin: 0;
    padding: 0;
    width: 1200px;
    height: 843px;
    overflow: hidden;
    background: var(--paper);
  }
  .card {
    position: relative;
    width: 1200px;
    height: 843px;
    background: var(--paper);
    overflow: hidden;
    font-family: "Noto Sans", Tahoma, sans-serif;
    color: var(--ink);
  }
  .card__art {
    position: absolute;
    inset: 0;
  }
  .identity {
    position: absolute;
    left: 499px;
    top: 540px;
    font-weight: 700;
    font-size: 28px;
    line-height: 38px;
  }
  .identity__line { display: flex; align-items: baseline; gap: 12px; white-space: nowrap; }
  .identity__ar {
    font-family: "Noto Sans Arabic", Tahoma, sans-serif;
    font-weight: 400;
    font-size: 27px;
  }
  .contact {
    position: absolute;
    left: 151px;
    top: 697px;
    margin: 0;
    font-size: 21px;
    line-height: 26.3px;
    letter-spacing: 0.6px;
  }
  .contact__row { display: flex; white-space: nowrap; }
  .contact__label { display: inline-block; width: 62px; }
  .brand {
    position: absolute;
    left: 840px;
    top: 752px;
    display: flex;
    align-items: center;
    gap: 16px;
    color: var(--brand-grey);
    font-size: 30px;
    font-weight: 400;
    letter-spacing: 0.5px;
  }
  .brand__dot {
    width: 56px;
    height: 56px;
    border-radius: 50%;
    background: var(--brand-blue);
  }
</style>
</head>
<body>
<main class="card">
  <svg class="card__art" width="1200" height="843" viewBox="0 0 1200 843" aria-hidden="true">
    <defs>
      <linearGradient id="bandFade" x1="0" x2="1" y1="0" y2="0">
        <stop offset="0" stop-color="#ffffff"/>
        <stop offset="0.3" stop-color="#f3f9fd"/>
        <stop offset="1" stop-color="#eef7fc"/>
      </linearGradient>
      <linearGradient id="bubbleFill" x1="0" x2="1" y1="0" y2="0">
        <stop offset="0" stop-color="#6cccf2"/>
        <stop offset="1" stop-color="#ffffff"/>
      </linearGradient>
      <linearGradient id="bubbleRim" x1="0" x2="1" y1="0" y2="0">
        <stop offset="0" stop-color="#949599"/>
        <stop offset="0.75" stop-color="#c9cacd"/>
        <stop offset="1" stop-color="#ffffff" stop-opacity="0"/>
      </linearGradient>
      <linearGradient id="ruleFade" x1="0" x2="1" y1="0" y2="0">
        <stop offset="0" stop-color="#8a8b8f"/>
        <stop offset="0.5" stop-color="#b9babd"/>
        <stop offset="1" stop-color="#ffffff"/>
      </linearGradient>
    </defs>
    <rect class="top-band" x="236" y="182" width="964" height="36" fill="url(#bandFade)"/>
    <circle class="bubble bubble--small" cx="625" cy="451" r="122" fill="url(#bubbleFill)" stroke="url(#bubbleRim)" stroke-width="5"/>
    <circle class="bubble bubble--large" cx="317" cy="668" r="172" fill="url(#bubbleFill)" stroke="url(#bubbleRim)" stroke-width="6"/>
    <rect class="rule" x="118" y="625" width="980" height="8" fill="url(#ruleFade)"/>
    <rect class="rule" x="118" y="643" width="980" height="8" fill="url(#ruleFade)"/>
    <rect class="rule" x="118" y="661" width="980" height="8" fill="url(#ruleFade)"/>
  </svg>

  <section class="identity">
    <div class="identity__line"><span>Marco Bellini</span><span class="identity__ar" lang="ar" dir="rtl">ماركو بيليني</span></div>
    <div class="identity__line"><span>Director of Operations</span><span class="identity__ar" lang="ar" dir="rtl">مدير العمليات</span></div>
  </section>

  <address class="contact" style="font-style:normal">
    <div class="contact__row"><span class="contact__label">M:</span><span>+962 79 555 0142</span></div>
    <div class="contact__row"><span class="contact__label">T&nbsp;&nbsp;:</span><span>+962 6 555 0187</span></div>
    <div class="contact__row"><span class="contact__label">F&nbsp;&nbsp;:</span><span>+962 6 555 0193</span></div>
    <div class="contact__row"><span class="contact__label">E&nbsp;&nbsp;:</span><span>mbellini@darnakheel-demo.com</span></div>
    <div class="contact__row"><span class="contact__label">W:</span><span>www.darnakheel-demo.com</span></div>
  </address>

  <div class="brand">
    <span>Dar Nakheel</span>
    <span class="brand__dot"></span>
  </div>
</main>
</body>
</html>
```